Need modern simple design for magazine ad, apartment and condo roofer.

I need a half page magazine ad for a local roofer to publish in an industry magazine. Apartment associations industry. All types of roofs. Shingle and Flat
Need the design to be creative and modern, clean and simple. I do not want a busy design. One that stands out and makes a point quickly.
Logo must be prominent.
DO NOT USE PHOTOS FROM MY WEBSITE PLEASE. Looking for something new.
I work on entire complexes not houses.

Need to make sure our phone number and email address are listed at the bottom. Here is my website www.vorbelan.com
Want to stay away from standard clip arts of tools, homes, apartment buildings.
Half Horizontal 7.25 x 4.75
Ads should be in PDF and JPG format.

Target Market(s)

Apartment or Condo owners looking for large scale roofing projects

Industry/Entity Type

Roofing

Requirements
Must have
• Prominent Logo
Simple Clean Design
Create graphics
Not Busy
Should not have
• Clip Art
No Photos from my website

```html
<!DOCTYPE html>
<html lang="en">
<head>
<meta charset="utf-8">
<title>Vorbelan Multifamily Roofing – Half Page Ad</title>
<link rel="stylesheet" href="https://fonts.googleapis.com/css2?family=Bebas+Neue&family=Arimo:wght@400&display=swap">
<style>
  :root {
    --brand-blue: #1f74b9;
    --ink: #111111;
    --paper: #ffffff;
    --stage: #4a4a4a;
    --sky-top: #2f7fc4;
    --sky-mid: #8fc0e6;
    --sky-light: #d9e9f5;
    --glass: #3d5f86;
    --tower: #25364f;
  }
  * { margin: 0; padding: 0; box-sizing: border-box; }
  html, body {
    width: 1200px;
    height: 837px;
    overflow: hidden;
    background: var(--stage);
  }
  .ad {
    position: absolute;
    left: 73px;
    top: 73px;
    width: 1054px;
    height: 690px;
    background: var(--paper);
    overflow: hidden;
  }
  .ad-shapes {
    position: absolute;
    inset: 0;
    width: 1054px;
    height: 690px;
  }
  .brand {
    position: absolute;
    left: 34px;
    top: 42px;
    display: flex;
    align-items: center;
    gap: 22px;
    color: var(--brand-blue);
    font-family: "Bebas Neue", "Arial Narrow", sans-serif;
    font-weight: 400;
  }
  .brand-mark {
    width: 118px;
    height: 118px;
    background: var(--brand-blue);
  }
  .brand-name {
    display: flex;
    flex-direction: column;
    line-height: 0.9;
  }
  .brand-name-main { font-size: 104px; letter-spacing: 2px; }
  .brand-name-sub { font-size: 33px; letter-spacing: 1.5px; }
  .headline {
    position: absolute;
    left: 36px;
    top: 322px;
    font-family: "Bebas Neue", "Arial Narrow", sans-serif;
    font-weight: 400;
    font-size: 75px;
    line-height: 72px;
    letter-spacing: 1px;
    color: var(--paper);
  }
  .headline .dark { color: var(--ink); }
  .web-address {
    position: absolute;
    left: 700px;
    top: 429px;
    width: 354px;
    height: 62px;
    display: flex;
    align-items: center;
    justify-content: center;
    font-family: "Bebas Neue", "Arial Narrow", sans-serif;
    font-size: 46px;
    letter-spacing: 1px;
    color: var(--paper);
  }
  .contact {
    position: absolute;
    left: 668px;
    top: 558px;
    font-family: "Arimo", Arial, sans-serif;
    font-size: 32px;
    color: var(--ink);
    list-style: none;
  }
  .contact-item {
    display: flex;
    align-items: center;
    gap: 10px;
    height: 46px;
  }
  .contact-icon { width: 28px; height: 28px; flex: none; }
</style>
</head>
<body>
  <main class="ad">
    <svg class="ad-shapes" viewBox="0 0 1054 690">
      <defs>
        <linearGradient id="sky" x1="0" y1="0" x2="1" y2="1">
          <stop offset="0" stop-color="var(--tower)"/>
          <stop offset="0.25" stop-color="var(--glass)"/>
          <stop offset="0.5" stop-color="var(--sky-top)"/>
          <stop offset="0.75" stop-color="var(--sky-mid)"/>
          <stop offset="1" stop-color="var(--sky-light)"/>
        </linearGradient>
        <linearGradient id="band-shadow" x1="0" y1="0" x2="0" y2="1">
          <stop offset="0" stop-color="#000" stop-opacity="0.18"/>
          <stop offset="1" stop-color="#000" stop-opacity="0"/>
        </linearGradient>
      </defs>
      <polygon class="photo-area" role="img"
        aria-label="Photo: upward view of tall modern glass apartment towers against a bright blue sky with light clouds"
        points="673,0 1054,0 1054,426 668,426 572,238"
        fill="url(#sky)"/>
      <polygon class="headline-panel" points="0,231 555,231 678,458 552,690 0,690" fill="var(--brand-blue)"/>
      <polygon class="web-band" points="688,426 1054,426 1054,491 690,491 707,458" fill="var(--brand-blue)"/>
      <rect class="web-band-shadow" x="690" y="491" width="364" height="14" fill="url(#band-shadow)"/>
    </svg>

    <div class="brand">
      <div class="brand-mark"></div>
      <div class="brand-name">
        <span class="brand-name-main">VORBELAN</span>
        <span class="brand-name-sub">MULTIFAMILY ROOFING</span>
      </div>
    </div>

    <h1 class="headline">
      ROOFS FOR ENTIRE<br>
      <span class="dark">APARTMENT COMPLEXES</span><br>
      <span class="dark">SHINGLE AND</span> FLAT ROOFS,<br>
      DONE RIGHT, ON TIME
    </h1>

    <p class="web-address">WWW.VORBELAN.COM</p>

    <ul class="contact">
      <li class="contact-item">
        <svg class="contact-icon" viewBox="0 0 28 28" aria-hidden="true">
          <circle cx="14" cy="14" r="12.5" fill="none" stroke="var(--brand-blue)" stroke-width="2.5"/>
          <path d="M9.5 7.5 L12 10.5 L10.8 12.2 C11.8 14.4 13.6 16.2 15.8 17.2 L17.5 16 L20.5 18.5 L18.8 20.7 C13.5 20.5 7.5 14.5 7.3 9.2 Z" fill="var(--brand-blue)"/>
        </svg>
        <span>555.214.0387</span>
      </li>
      <li class="contact-item">
        <svg class="contact-icon" viewBox="0 0 28 28" aria-hidden="true">
          <rect x="1" y="6" width="26" height="17" rx="1.5" fill="var(--brand-blue)"/>
          <path d="M2 7.5 L14 16 L26 7.5" fill="none" stroke="var(--paper)" stroke-width="2"/>
        </svg>
        <span>info@vorbelan.com</span>
      </li>
    </ul>
  </main>
</body>
</html>
```